Logo and Business Card Design

Harbor Vale Logistics provides our customers with one call solutions to packing, trucking and warehousing needs throughout the supply chain.
We need ideas for a logo/business card. I have 2 general concepts.
1. Modern logo involving: the globe, Harbor Vale, arrow, movement, the two words having 2 different fonts/colors, the number 1.
2. Logo involving Lion/Winged Lion: incorporate lion onto globe, tagline "The Crest of the Herd", movement, flowing.

Target Market(s)

International Logistics companies, Air cargo companies, manufacturing companies

Industry/Entity Type

Business

Contact Information for Business Card

Dale Whitfield
Owner
Harbor Vale Logistics
2874 Maren Ave.
Elk Grove Village, IL 60029
847-539-2864
daleh@harborvalefreight.example

Font styles to use
Sans Serif

Requirements
Must have
• 1. Modern logo involving: the globe, Harbor Vale, arrow, movement, the two words having 2 different fonts/colors, the number 1.
Nice to have
Should not have
• Do not have too complex of a design.

```html
<!DOCTYPE html>
<html lang="en">
<head>
<meta charset="utf-8">
<title>Harbor Vale Logistics – Business Card</title>
<link rel="stylesheet" href="https://fonts.googleapis.com/css2?family=Source+Sans+3:wght@400;600&display=swap">
<style>
  :root {
    --backdrop: #2a2a2c;
    --card-dark: #1c1c1e;
    --card-dark-edge: #2e2e31;
    --card-light: #ffffff;
    --card-light-shade: #eef0f2;
    --brand-blue: #1ea9e8;
    --brand-grey: #8a8c8f;
    --ink: #2b2b2b;
    --faint: #e6e7e9;
    --band-grey: #b9bbbe;
  }
  * { box-sizing: border-box; margin: 0; padding: 0; }
  html, body { width: 1200px; height: 900px; overflow: hidden; }
  body {
    background: var(--backdrop);
    font-family: "Source Sans 3", "Helvetica Neue", Arial, sans-serif;
    position: relative;
  }
  .card {
    position: absolute;
    width: 525px;
    height: 300px;
    border-radius: 22px;
    overflow: hidden;
    box-shadow: 0 18px 40px rgba(0,0,0,.45);
  }
  /* Back side */
  .card-back {
    left: 337px; top: 95px;
    background: linear-gradient(160deg, var(--card-dark-edge), var(--card-dark) 60%);
    display: flex; flex-direction: column; align-items: center; justify-content: center;
  }
  .back-mark {
    width: 78px; height: 78px; border-radius: 50%;
    border: 4px solid var(--brand-grey);
    margin-bottom: 14px;
  }
  .back-name {
    color: var(--brand-blue);
    font-weight: 600;
    font-size: 32px;
    letter-spacing: 2px;
    text-transform: uppercase;
    line-height: 1;
  }
  .back-tagline {
    color: var(--brand-grey);
    font-size: 15px;
    font-weight: 600;
    margin-top: 6px;
  }
  /* Front side */
  .card-front {
    left: 337px; top: 475px;
    background: linear-gradient(180deg, var(--card-light), var(--card-light-shade));
  }
  .front-decor { position: absolute; inset: 0; }
  .front-logo {
    position: absolute; left: 36px; top: 36px;
    display: flex; align-items: center; gap: 14px;
  }
  .front-logo-mark {
    width: 54px; height: 54px; border-radius: 50%;
    border: 3px solid var(--brand-grey);
  }
  .front-logo-divider { width: 1px; height: 48px; background: var(--band-grey); }
  .front-logo-name {
    color: var(--brand-blue);
    font-weight: 600;
    font-size: 21px;
    letter-spacing: 1px;
    line-height: 1;
    text-transform: uppercase;
    display: flex; flex-direction: column;
  }
  .holder {
    position: absolute; left: 36px; top: 148px;
    color: var(--ink); font-size: 13px; line-height: 1.3;
  }
  .holder-name { color: var(--brand-blue); font-size: 20px; line-height: 1.1; }
  .holder-role { margin-bottom: 12px; }
  .contact {
    position: absolute; left: 300px; top: 108px;
    list-style: none; color: var(--ink); font-size: 12.5px; line-height: 1.55;
  }
  .contact li { display: flex; align-items: center; gap: 6px; }
  .contact svg { width: 11px; height: 11px; flex: none; }
  .contact .web { color: var(--brand-blue); }
</style>
</head>
<body>

<section class="card card-back" aria-label="Card back">
  <div class="back-mark"></div>
  <div class="back-name">Harbor Vale</div>
  <div class="back-tagline">The Crest of the Herd</div>
</section>

<section class="card card-front" aria-label="Card front">
  <svg class="front-decor" viewBox="0 0 525 300" aria-hidden="true">
    <circle cx="410" cy="105" r="135" fill="none" stroke="var(--faint)" stroke-width="14"/>
    <polygon points="300,300 525,205 525,300" fill="var(--band-grey)"/>
    <polygon points="290,290 525,185 525,205 320,300 300,300" fill="var(--brand-blue)"/>
    <rect x="0" y="282" width="525" height="18" fill="var(--band-grey)"/>
  </svg>

  <div class="front-logo">
    <div class="front-logo-mark"></div>
    <div class="front-logo-divider"></div>
    <div class="front-logo-name"><span>Harbor</span><span>Vale</span></div>
  </div>

  <div class="holder">
    <div class="holder-name">Dale Whitfield</div>
    <div class="holder-role">Owner</div>
    <div>Harbor Vale Logistics</div>
    <div>2874 Maren Ave. Elk Grove Village,</div>
    <div>IL 60029</div>
  </div>

  <ul class="contact">
    <li>
      <svg viewBox="0 0 12 12"><rect x="1" y="1" width="10" height="10" rx="2" fill="var(--brand-blue)"/><path d="M4 3.5l1 1-1 1.2c.6 1 1.3 1.7 2.3 2.3l1.2-1 1 1-1 1.5C5 8.8 3.2 7 3 4.5z" fill="#fff"/></svg>
      847-539-2864
    </li>
    <li>
      <svg viewBox="0 0 12 12"><rect x="0.5" y="2" width="11" height="8" rx="1" fill="var(--brand-blue)"/><path d="M1 2.5l5 4 5-4" stroke="#fff" fill="none"/></svg>
      daleh@harborvalefreight.example
    </li>
    <li>
      <svg viewBox="0 0 12 12"><circle cx="6" cy="6" r="5.5" fill="var(--brand-blue)"/><path d="M1 6h10M6 1c-2 2.5-2 7.5 0 10M6 1c2 2.5 2 7.5 0 10" stroke="#fff" stroke-width=".8" fill="none"/></svg>
      <span>www.<span class="web">harborvalefreight.example</span></span>
    </li>
  </ul>
</section>

</body>
</html>
```